business card

Business card for new business.
Red and black corporate colors.
Card can have an Indsutrial feel to it. Feel free to add Rust, Bolted steel, or graphics as you see fit. We provide highly specialized services to the below mentioned industries.
Keep information out of corners so that if I want I can choose rounded corners.
Information
- front. name - title - phone - email
- Rear
Refining - Rail - Infrastructure - Mining - Energy
Calgary - Edmonton - Fort McMurray - Revelstoke - Vancouver

```html
<!DOCTYPE html>
<html lang="en">
<head>
<meta charset="utf-8">
<title>Girderline Business Card</title>
<link rel="stylesheet" href="https://fonts.googleapis.com/css2?family=Arimo:wght@400;700&display=swap">
<style>
  :root {
    --stage: #1c1c1f;
    --card: #050505;
    --red: #e5262b;
    --grey: #a7a7a7;
    --grey-dark: #8a8a8a;
  }
  * { margin: 0; padding: 0; box-sizing: border-box; }
  html, body { width: 1200px; height: 800px; overflow: hidden; background: var(--stage); }
  body { font-family: "Arimo", Arial, sans-serif; }
  .stage {
    width: 1200px; height: 800px;
    display: flex; align-items: center; justify-content: center; gap: 40px;
  }
  .card {
    width: 540px; height: 309px;
    background: var(--card);
    position: relative;
    box-shadow: 0 18px 40px rgba(0,0,0,.55);
  }
  .brand { display: flex; align-items: center; gap: 10px; }
  .brand-mark { width: 16px; height: 16px; background: var(--red); }
  .brand-name {
    font-weight: 700; font-size: 40px; letter-spacing: 1px;
    color: var(--grey);
  }
  /* rear */
  .card-rear { display: flex; flex-direction: column; align-items: center; justify-content: center; }
  .card-rear .brand { margin-bottom: 34px; }
  .sector-list, .city-list {
    font-size: 15px; color: var(--grey-dark); line-height: 22px; text-align: center;
  }
  .sep { color: var(--red); padding: 0 4px; }
  /* front */
  .card-front .brand { position: absolute; left: 48px; top: 160px; transform: translateY(-50%); }
  .card-front .brand-name { font-size: 34px; }
  .divider {
    position: absolute; left: 318px; top: 70px; width: 1px; height: 170px;
    background: linear-gradient(var(--card), var(--red), var(--card));
  }
  .contact { position: absolute; left: 338px; top: 78px; color: var(--grey); font-size: 13px; line-height: 18px; }
  .person-name { color: var(--red); font-size: 17px; line-height: 20px; font-weight: 400; }
  .person-title { color: var(--grey); font-size: 13px; margin-bottom: 14px; }
  .address { margin-bottom: 6px; }
  .contact-row { display: flex; align-items: center; gap: 7px; }
  .contact-row svg { width: 11px; height: 11px; fill: var(--red); flex: none; }
</style>
</head>
<body>
<main class="stage">
  <section class="card card-rear">
    <div class="brand">
      <span class="brand-mark"></span>
      <span class="brand-name">GIRDERLINE</span>
    </div>
    <p class="sector-list">Welding<span class="sep">|</span>Rigging<span class="sep">|</span>Fabrication<span class="sep">|</span>Piping<span class="sep">|</span>Power</p>
    <p class="city-list">Ashford<span class="sep">|</span>Coldwater<span class="sep">|</span>Port Halden<span class="sep">|</span>Millbrook<span class="sep">|</span>Stonehaven</p>
  </section>

  <section class="card card-front">
    <div class="brand">
      <span class="brand-mark"></span>
      <span class="brand-name">GIRDERLINE</span>
    </div>
    <span class="divider"></span>
    <div class="contact">
      <h1 class="person-name">MARA ELLISON</h1>
      <p class="person-title">Managing Director</p>
      <p class="address">PO BOX 47 Kiln Road<br>2nd street Harlow ,USA</p>
      <p class="contact-row">
        <svg viewBox="0 0 24 24"><path d="M6.6 10.8a15 15 0 0 0 6.6 6.6l2.2-2.2a1 1 0 0 1 1-.25 11.4 11.4 0 0 0 3.6.57 1 1 0 0 1 1 1V20a1 1 0 0 1-1 1A17 17 0 0 1 3 4a1 1 0 0 1 1-1h3.5a1 1 0 0 1 1 1c0 1.25.2 2.45.57 3.57a1 1 0 0 1-.25 1z"/></svg>
        (01) 5550 1234
      </p>
      <p class="contact-row">
        <svg viewBox="0 0 24 24"><path d="M2 5h20v14H2z M2 5l10 8 10-8" stroke="#050505" stroke-width="1.5"/></svg>
        info@girderline.com
      </p>
      <p class="contact-row">
        <svg viewBox="0 0 24 24"><circle cx="12" cy="12" r="10"/><path d="M2 12h20M12 2c3 3 3 17 0 20M12 2c-3 3-3 17 0 20" stroke="#050505" stroke-width="1.5" fill="none"/></svg>
        www.girderline.com
      </p>
    </div>
  </section>
</main>
</body>
</html>
```